Wealth management firm needs a business card design

Using my logo, create a business card that covers all of the regulatory wordings that I need. It must have - Registered Office 7-9 Pelgrove Wynd, Edinburgh, EH4 2QN. Registered in Scotland under number SC804317. VORELT Wealth Management Ltd is an appointed representative of Kestoby wealth management Ltd, which is authorised and regulated by the Monetary Oversight Council.

Target Market(s)

professional clients

Industry/Entity Type

finance

Contact Information for Business Card

VORELT Wealth Management, Conor Tresk-Whitlaw, Director, 5 Dunmore Row, Edinburgh, EH9 4RT. 07812 459 163, conor.tresk-whitlaw@vorelt-example.com , www.vorelt-example.com

Font styles to use
Serif

Colors
0054AA
0677BA
7BADD7
CADEEF
E8F1F8

Requirements
Must have
• regulatory wording in small text at bottom

```html
<!DOCTYPE html>
<html lang="en">
<head>
<meta charset="utf-8">
<title>VORELT Wealth Management – Business Card</title>
<link rel="stylesheet" href="https://fonts.googleapis.com/css2?family=Noto+Serif:wght@400;700&display=swap">
<style>
  :root {
    --stage: #1c1c1f;
    --card-light: #ffffff;
    --card-dark: #1f2029;
    --brand-blue: #2f6db5;
    --brand-blue-soft: #3a78c4;
    --ink: #1d1d22;
    --ink-inverse: #ffffff;
    --ink-muted: #a9adbb;
  }
  * { margin: 0; padding: 0; box-sizing: border-box; }
  html, body {
    width: 1200px; height: 1059px; overflow: hidden;
    background: var(--stage);
    font-family: "Noto Serif", Georgia, serif;
  }
  .canvas { position: relative; width: 1200px; height: 1059px; }

  .card {
    position: absolute;
    border-radius: 18px;
    overflow: hidden;
  }
  .card--front { left: 257px; top: 89px; width: 687px; height: 390px; background: var(--card-light); color: var(--ink); }
  .card--back  { left: 254px; top: 547px; width: 693px; height: 393px; background: var(--card-dark); color: var(--ink-inverse); }

  .centered { position: absolute; left: 0; right: 0; text-align: center; white-space: nowrap; }

  .brand-mark {
    position: absolute; border-radius: 50%; background: var(--brand-blue);
  }
  .card--front .brand-mark { width: 70px; height: 70px; left: 308px; top: 55px; }
  .card--back .brand-mark  { width: 92px; height: 92px; left: 300px; top: 84px; }

  .company-name { font-weight: 400; line-height: 1; }
  .card--front .company-name { top: 140px; font-size: 21.5px; }
  .card--back  .company-name { top: 204px; font-size: 29px; }

  .tagline { line-height: 1; }
  .card--front .tagline { top: 167px; font-size: 9px; }
  .card--back  .tagline { top: 240px; font-size: 12.5px; }

  .person {
    position: absolute; right: 395px; top: 234px; text-align: right; white-space: nowrap;
  }
  .person__name { font-size: 23px; font-weight: 700; color: var(--brand-blue); line-height: 1.1; }
  .person__role { font-size: 15px; line-height: 1.3; }

  .divider {
    position: absolute; left: 307px; top: 227px; width: 1px; height: 62px; background: var(--brand-blue);
  }

  .contact-list { position: absolute; left: 324px; top: 220px; list-style: none; }
  .contact-list li {
    display: flex; align-items: center; height: 26px;
    font-size: 15.5px; white-space: nowrap;
  }
  .contact-list svg { width: 12px; height: 12px; margin-right: 7px; flex: none; fill: var(--brand-blue); }

  .card--front .address { top: 328px; font-size: 15.5px; line-height: 1; }

  .card--back .registered-office { top: 300px; font-size: 16.5px; line-height: 1; }
  .card--back .registration-number { top: 326px; font-size: 16px; line-height: 1; color: var(--brand-blue-soft); }
  .card--back .regulatory-note {
    top: 352px; left: 60px; right: 60px;
    white-space: normal; font-size: 8.5px; line-height: 1.35; color: var(--ink-muted);
  }
</style>
</head>
<body>
<main class="canvas">

  <section class="card card--front" aria-label="Business card front">
    <span class="brand-mark" aria-hidden="true"></span>
    <h1 class="centered company-name">VORELT Wealth Management Ltd</h1>
    <p class="centered tagline">Personal Financial Advice</p>

    <div class="person">
      <p class="person__name">Conor Tresk-Whitlaw</p>
      <p class="person__role">Director</p>
    </div>
    <span class="divider" aria-hidden="true"></span>

    <ul class="contact-list">
      <li>
        <svg viewBox="0 0 24 24" aria-hidden="true"><path d="M6.6 10.8a15.1 15.1 0 0 0 6.6 6.6l2.2-2.2c.3-.3.7-.4 1-.2 1.1.4 2.3.6 3.6.6.6 0 1 .4 1 1V20c0 .6-.4 1-1 1A17 17 0 0 1 3 4c0-.6.4-1 1-1h3.5c.6 0 1 .4 1 1 0 1.3.2 2.5.6 3.6.1.3 0 .7-.2 1z"/></svg>
        07812 459 163
      </li>
      <li>
        <svg viewBox="0 0 24 24" aria-hidden="true"><path d="M2 5h20v14H2z M4 7v.5l8 5.5 8-5.5V7z" fill-rule="evenodd"/></svg>
        conor.tresk-whitlaw@vorelt-example.com
      </li>
      <li>
        <svg viewBox="0 0 24 24" aria-hidden="true"><path d="M12 2a10 10 0 1 0 0 20 10 10 0 0 0 0-20zm6.9 6h-3a15 15 0 0 0-1.3-3.8A8 8 0 0 1 18.9 8zM12 4c.8 1.2 1.5 2.5 1.9 4h-3.8c.4-1.5 1.1-2.8 1.9-4zM4.3 14a8 8 0 0 1 0-4h3.4a16 16 0 0 0 0 4zm.8 2h3a15 15 0 0 0 1.3 3.8A8 8 0 0 1 5.1 16zm3-8h-3a8 8 0 0 1 4.3-3.8A15 15 0 0 0 8.1 8zM12 20c-.8-1.2-1.5-2.5-1.9-4h3.8c-.4 1.5-1.1 2.8-1.9 4zm2.3-6H9.7a14 14 0 0 1 0-4h4.6a14 14 0 0 1 0 4zm.3 5.8a15 15 0 0 0 1.3-3.8h3a8 8 0 0 1-4.3 3.8zm1.7-5.8a16 16 0 0 0 0-4h3.4a8 8 0 0 1 0 4z"/></svg>
        www.vorelt-example.com
      </li>
    </ul>

    <p class="centered address">5 Dunmore Row, Edinburgh, EH9 4RT</p>
  </section>

  <section class="card card--back" aria-label="Business card back">
    <span class="brand-mark" aria-hidden="true"></span>
    <h2 class="centered company-name">VORELT Wealth Management Ltd</h2>
    <p class="centered tagline">Personal Financial Advice</p>
    <p class="centered registered-office">Registered Office 7-9 Pelgrove Wynd, Edinburgh, EH4 2QN</p>
    <p class="centered registration-number">Registered in Scotland under number SC804317</p>
    <p class="centered regulatory-note">VORELT Wealth Management Ltd is an appointed representative of Kestoby wealth management Ltd, which is authorised and regulated by the Monetary Oversight Council.</p>
  </section>

</main>
</body>
</html>
```